Criminal Defense law firm needs website and logo

Need a logo design and web design for a small firm in Miami, Florida. The firm concentrates in the areas of state and federal criminal defense in Miami Dade County, Florida.The firm handles cases in the areas of Drug Possession, Fraud Offenses, Traffic Offenses, domestic violence, Violent Crimes, probation violation, Juvenile Delinquency, and expunction/expungment of criminal records (detailed list provided in attachment). The name of the attorney is Loreta Benavides-Kurtz. Sole Practitioner. Will attach profile. (the attachment are from my previous law firm, can use any of the language but adjust to a sole practitioner)

Industry/Entity Type

Lawyer

Number of Pages Required

3 page

Font styles to use
Serif

Colors
0356a4

Requirements
Must have
• Page that includes area's of practice. Page for Attorney profile. Contact page indicating that we speak Spanish and accept all major credit cards.

```html
<!DOCTYPE html>
<html lang="en">
<head>
<meta charset="utf-8">
<title>Benavides Kurtz Law</title>
<link rel="stylesheet" href="https://fonts.googleapis.com/css2?family=Roboto:wght@300;400;500;700&family=Lato:ital,wght@0,400;1,400&display=swap">
<style>
:root{
  --brand:#0356a4;
  --brand-dark:#02478a;
  --ink:#222;
  --text:#555;
  --muted:#999;
  --line:#e4e4e4;
  --light:#f0f0f0;
  --footer:#eeeeee;
  --white:#fff;
}
*{margin:0;padding:0;box-sizing:border-box}
html,body{width:1200px;height:2946px;overflow:hidden;background:var(--white)}
body{position:relative;font-family:'Roboto',sans-serif;color:var(--text)}
.abs{position:absolute}
.italic{font-family:'Lato',sans-serif;font-style:italic}

/* hero */
.hero{left:0;top:0;width:1200px;height:670px;background:linear-gradient(110deg,#6c5a4a 0%,#9a8574 30%,#4d4f57 62%,#2a2a30 100%)}
.hero-shade{left:0;top:0;width:1200px;height:670px;background:rgba(0,0,0,.28)}
.nav-bar{left:0;top:0;width:1200px;height:78px;border-bottom:1px solid rgba(255,255,255,.18)}
.logo{left:75px;top:22px;font-size:29px;font-weight:400;color:var(--white)}
.nav{right:72px;top:34px;display:flex;gap:30px;font-size:13px;font-weight:500;color:var(--white);align-items:center}
.nav .lang{font-weight:400;color:#ddd;padding-left:14px;border-left:1px solid rgba(255,255,255,.3)}
.nav .lang b{color:#4e9be6;font-weight:400}
.hero-title{left:0;top:318px;width:1200px;text-align:center;color:var(--white);font-size:40px;font-weight:400;line-height:48px}
.hero-sub{left:245px;top:430px;width:710px;text-align:center;color:#eee;font-size:15px;line-height:24px}
.arrow{width:50px;height:50px;border:2px solid var(--white);border-radius:50%;top:306px}
.arrow.left{left:77px}
.arrow.right{left:1077px;border-color:rgba(255,255,255,.35)}

/* call bar */
.call-bar{left:75px;top:703px;width:1050px;height:63px;background:var(--brand);color:var(--white);display:flex;align-items:center}
.call-bar .phone-ic{margin-left:22px}
.call-bar .label{margin-left:30px;font-size:19px;font-weight:500}
.call-bar .label b{font-size:25px;font-weight:500;margin-left:6px}
.call-bar .sep{width:1px;height:38px;background:rgba(255,255,255,.5);margin-left:24px}
.call-bar .hours{margin-left:24px;font-size:18px}

/* about */
.eyebrow{left:75px;top:828px;font-size:23px;color:var(--ink)}
.about-title{left:75px;top:855px;font-size:27px;color:var(--brand)}
.about-copy{left:75px;top:905px;width:680px;font-size:13.5px;line-height:22px;color:var(--text)}
.about-copy p+p{margin-top:18px}
.btn{background:var(--brand);color:var(--white);font-size:14px;font-weight:500;display:flex;align-items:center;justify-content:center}
.read-more{left:75px;top:1082px;width:153px;height:41px}
.photo-frame{left:919px;top:813px;width:206px;height:338px;background:linear-gradient(135deg,#1b5fa8,#0b3f80)}
.photo-frame-line{left:937px;top:827px;width:172px;height:311px;border:1px solid rgba(255,255,255,.35)}
.attorney-photo{left:837px;top:858px;width:171px;height:248px;border:5px solid var(--white);background:linear-gradient(180deg,#6b6f75 0%,#4a3a33 45%,#222 100%)}
.divider{left:75px;top:1196px;width:1050px;height:1px;background:var(--line)}

/* practice areas */
.section-title{font-size:28px;color:var(--ink);font-weight:400}
.practice-title{left:75px;top:1232px}
.practice-sub{left:75px;top:1288px;font-size:15px;line-height:24px;color:#555}
.dots{left:1096px;top:1313px;display:flex;gap:5px}
.dots span{width:11px;height:11px;border-radius:50%;background:#ccc}
.dots span:first-child{background:var(--brand)}
.cards{left:0;top:1355px;width:1200px;height:324px;display:flex}
.card{width:240px;height:324px;border:1px solid var(--line);border-left:none;padding:30px 0 0 30px;position:relative}
.card:first-child{border-left:1px solid var(--line)}
.card .icon{height:56px}
.card h3{margin-top:14px;font-size:20px;font-weight:400;color:var(--ink);line-height:25px;height:60px}
.card p{margin-top:22px;font-size:13.5px;line-height:22px;color:#666;width:175px}
.card.active{background:var(--brand);border-color:var(--brand)}
.card.active h3,.card.active p{color:var(--white)}
.underline{width:52px;height:2px;background:var(--brand)}

/* news */
.news-title{left:75px;top:1740px}
.news-item{left:75px;width:490px;height:130px}
.news-thumb{left:0;top:0;width:153px;height:110px}
.news-item h4{position:absolute;left:171px;top:-2px;font-size:20px;font-weight:400;color:var(--brand)}
.news-meta{position:absolute;left:171px;top:28px;font-size:12px;color:var(--muted)}
.news-item p{position:absolute;left:171px;top:50px;width:320px;font-size:13px;line-height:21px;color:#555}
.news-sep{left:75px;top:1958px;width:490px;height:1px;background:var(--line)}

/* testimonial */
.clients-title{left:615px;top:1736px}
.quote-box{left:615px;top:1811px;width:510px;height:285px;background:var(--light)}
.quote-text{left:34px;top:40px;width:444px;font-size:15.5px;line-height:25px;color:#666;text-indent:56px;text-align:justify}
.quote-mark{left:32px;top:34px}
.q-line{left:34px;top:174px;width:40px;height:2px;background:var(--brand)}
.client-avatar{left:30px;top:193px;width:62px;height:62px;border-radius:50%;border:3px solid var(--white);background:linear-gradient(160deg,#c9a58a,#6f5a4e)}
.client-name{left:104px;top:207px;font-size:13px;color:#444}
.client-role{left:104px;top:229px;font-size:10px;color:var(--muted)}

/* consultation form */
.consult{left:0;top:2176px;width:1200px;height:440px;background:linear-gradient(120deg,#1c1c1e 0%,#2b2c30 45%,#3a3a3c 70%,#1e1e20 100%)}
.consult-shade{left:0;top:2176px;width:1200px;height:440px;background:rgba(0,0,0,.35)}
.consult-title{left:75px;top:2226px;font-size:28px;color:var(--white)}
.consult-sub{left:75px;top:2272px;font-size:15px;line-height:24px;color:#ddd}
.field{top:2348px;width:242px;border-bottom:2px solid #ddd;height:30px;font-size:12.5px;color:#eee}
.field.desc{left:75px;top:2420px;width:1050px;height:62px}
.send{left:505px;top:2510px;width:190px;height:46px;font-size:15px}

/* footer */
.footer{left:0;top:2616px;width:1200px;height:271px;background:var(--footer)}
.f-head{font-size:16px;font-weight:500;color:var(--brand);top:2662px}
.f-list{left:75px;top:2697px;font-size:13px;line-height:27.5px;color:#333;list-style:none}
.f-list li::before{content:"";display:inline-block;width:5px;height:5px;border-radius:50%;background:var(--brand);margin:0 11px 2px 5px}
.f-text{font-size:13px;line-height:20px;color:#333}
.email-input{left:267px;top:2747px;width:215px;height:34px;background:#ddd;font-size:12px;color:#999;padding:10px 15px}
.subscribe{left:267px;top:2794px;width:123px;height:32px;font-size:12.5px}
.contact-row{left:575px;display:flex;align-items:center;gap:10px;font-size:14px;color:var(--brand)}
.f-logo{left:900px;top:2660px;font-size:22px;color:#333}
.social{left:900px;top:2748px;display:flex;gap:9px}
.social span{width:29px;height:29px;background:#9a9a9a}
.copy-bar{left:0;top:2887px;width:1200px;height:59px;background:var(--brand);color:var(--white);font-size:13px;text-align:center;line-height:59px}
</style>
</head>
<body>

<!-- hero -->
<div class="abs hero" role="img" aria-label="Photo of smiling clients shaking hands with an attorney across a desk"></div>
<div class="abs hero-shade"></div>
<div class="abs nav-bar"></div>
<div class="abs logo">Benavides Kurtz Law</div>
<nav class="abs nav">
  <span>HOME</span><span>ABOUT US</span><span>ATTORNEY</span><span>PRACTICE AREAS</span><span>BLOG</span><span>CONTACT US</span>
  <span class="lang"><b>Eng</b> / Spn</span>
</nav>
<div class="abs arrow left">
  <svg width="46" height="46" viewBox="0 0 46 46"><path d="M26 15 L18 23 L26 31" fill="none" stroke="#fff" stroke-width="2"/></svg>
</div>
<div class="abs arrow right">
  <svg width="46" height="46" viewBox="0 0 46 46"><path d="M20 15 L28 23 L20 31" fill="none" stroke="rgba(255,255,255,.5)" stroke-width="2"/></svg>
</div>
<h1 class="abs hero-title">WE OFFER OUR CLENTS ONLY<br>EXPERT LEGAL ADVICE</h1>
<p class="abs hero-sub italic">Lorem ipsum dolor sit amet, cons ectetur elit. Vestibulum nec odios Suspe ndisse cursus mal suada faci lisis. Lorem ipsum dolor sit ametion consectetur elit. Vesti bulum nec odio ipsum.</p>
<svg class="abs" style="left:572px;top:494px" width="56" height="44" viewBox="0 0 56 44">
  <g fill="none" stroke="#fff" stroke-width="2.5">
    <line x1="28" y1="3" x2="28" y2="38"/><line x1="8" y1="10" x2="48" y2="10"/>
    <line x1="18" y1="40" x2="38" y2="40"/>
    <path d="M8 10 L2 24 H14 Z"/><path d="M48 10 L42 24 H54 Z"/>
  </g>
  <circle cx="28" cy="4" r="3" fill="#fff"/>
</svg>

<!-- call bar -->
<div class="abs call-bar">
  <svg class="phone-ic" width="30" height="30" viewBox="0 0 24 24"><path d="M6.6 3.5l2.6 3.4-1.6 2.1c1 2.2 2.8 4 5 5l2.1-1.6 3.4 2.6-1.6 3.2c-7 -.4-12.5-6-12.9-12.9z" fill="none" stroke="#fff" stroke-width="1.5" stroke-linejoin="round"/></svg>
  <span class="label">GET FREE LEGAL CONSULTATNT: <b>1800 555 0142</b></span>
  <span class="sep"></span>
  <span class="hours italic">7 Days A Week From : 8.00 Am To 2.30 Pm</span>
</div>

<!-- about -->
<div class="abs eyebrow">ABOUT</div>
<h2 class="abs about-title" style="font-weight:400">Benavides Kurtz Law</h2>
<div class="abs about-copy">
  <p>Lorem ipsum dolor sit amet, cons ectetur elit. Vestibulum nec odios Suspe ndisse cursus mal suada faci lisis. Sed ut perspiciatis unde omnis iste natus error sit voluptatem accusa nt ium doloremque lau dantium totam rem aperiam. Vestibulum nec odios Suspe ndisse cursus mal suada faci lisis. Lorem ipsum dolor sit ametion consectetur elit. Vesti bulum nec odio ipsum. &nbsp;voluptatem accusa nt ium doloremque</p>
  <p>Sed ut perspiciatis unde omnis iste natus error sit voluptatem accusa nt ium doloremque lau dantium totam rem aperiam Sed ut perspiciatis unde omnis iste natus error sit voluptatem accusa nt ium doloremque</p>
</div>
<div class="abs btn read-more">READ MORE</div>
<div class="abs photo-frame" role="img" aria-label="Blue toned decorative photo of a classical column"></div>
<div class="abs photo-frame-line"></div>
<div class="abs attorney-photo" role="img" aria-label="Portrait photo of the attorney"></div>
<div class="abs divider"></div>

<!-- practice areas -->
<h2 class="abs section-title practice-title">Practice Areas</h2>
<p class="abs practice-sub italic">Suspe ndisse cursus mal suada faci lisis. Lorem ipsum dolor sit ametion consectetur elit.<br>Vesti bulum nec odio ipsum voluptatem accusa nt ium doloremque</p>
<div class="abs dots"><span></span><span></span></div>

<div class="abs cards">
  <div class="card">
    <svg class="icon" width="56" height="56" viewBox="0 0 56 56"><g transform="rotate(-40 28 28)"><rect x="6" y="18" width="44" height="20" rx="10" fill="none" stroke="#0356a4" stroke-width="3"/><path d="M28 18 H40 a10 10 0 0 1 0 20 H28z" fill="#0356a4"/></g></svg>
    <h3>Drug<br>Possession</h3>
    <p>Nemo enim ipsam voluptatem quia voluptas sit aspernatur aut odit aut fugit sed quia conse.</p>
  </div>
  <div class="card active">
    <svg class="icon" width="56" height="56" viewBox="0 0 56 56"><g fill="none" stroke="#fff" stroke-width="2.5"><rect x="8" y="8" width="32" height="42"/><line x1="14" y1="18" x2="34" y2="18"/><line x1="14" y1="26" x2="34" y2="26"/><line x1="14" y1="34" x2="28" y2="34"/><line x1="34" y1="42" x2="50" y2="12"/></g></svg>
    <h3>Fraud<br>Offenses</h3>
    <p>Nemo enim ipsam voluptatem quia voluptas sit aspernatur aut odit aut fugit sed quia conse.</p>
  </div>
  <div class="card">
    <svg class="icon" width="56" height="56" viewBox="0 0 56 56"><g fill="#0356a4"><circle cx="16" cy="16" r="8"/><rect x="6" y="26" width="20" height="22" rx="6"/><circle cx="40" cy="22" r="8"/><rect x="30" y="32" width="20" height="18" rx="6"/></g></svg>
    <h3>Domestic<br>Violence</h3>
    <p>Nemo enim ipsam voluptatem quia voluptas sit aspernatur aut odit aut fugit sed quia conse.</p>
  </div>
  <div class="card">
    <svg class="icon" width="56" height="56" viewBox="0 0 56 56"><g fill="none" stroke="#0356a4" stroke-width="3"><circle cx="15" cy="34" r="11"/><circle cx="41" cy="34" r="11"/><path d="M22 18 Q28 10 34 18"/></g></svg>
    <h3>Violent<br>Crimes</h3>
    <p>Nemo enim ipsam voluptatem quia voluptas sit aspernatur aut odit aut fugit sed quia conse.</p>
  </div>
  <div class="card">
    <svg class="icon" width="56" height="56" viewBox="0 0 56 56"><g fill="#0356a4"><circle cx="18" cy="10" r="6"/><rect x="10" y="19" width="16" height="32" rx="3"/><circle cx="38" cy="16" r="5"/><rect x="31" y="24" width="14" height="27" rx="3"/></g></svg>
    <h3>Juvenile<br>Delinquency</h3>
    <p>Nemo enim ipsam voluptatem quia voluptas sit aspernatur aut odit aut fugit sed quia conse.</p>
  </div>
</div>

<!-- legal news -->
<h2 class="abs section-title news-title">Legal News</h2>
<div class="abs underline" style="left:75px;top:1783px"></div>

<article class="abs news-item" style="top:1815px">
  <div class="abs news-thumb" role="img" aria-label="Photo of business people silhouetted against a window" style="background:linear-gradient(180deg,#dfe4ea,#8e99a6 60%,#3d4650)"></div>
  <h4>In the world crime only is lose</h4>
  <div class="news-meta">23 November, 2015 &nbsp;// &nbsp;By Daniel Herrera</div>
  <p>Vero eos et accusamus et iusto odio dignissimos duci qui blanditiis praesentium voluptatum deleniti atque corrupti quos dolores et quas.</p>
</article>
<div class="abs news-sep"></div>
<article class="abs news-item" style="top:1986px">
  <div class="abs news-thumb" role="img" aria-label="Photo of a justice statue beside law books" style="background:linear-gradient(90deg,#e7e2da 0%,#b6a58f 45%,#5a3b2a 75%,#2a1d18 100%)"></div>
  <h4>We may brave human laws</h4>
  <div class="news-meta">23 November, 2015 &nbsp;// &nbsp;By Daniel Herrera</div>
  <p>Vero eos et accusamus et iusto odio dignissimos duci qui blanditiis praesentium voluptatum deleniti atque corrupti quos dolores et quas.</p>
</article>

<!-- happy clients -->
<h2 class="abs section-title clients-title">Happy Clients</h2>
<div class="abs underline" style="left:615px;top:1779px"></div>
<div class="abs quote-box">
  <svg class="abs quote-mark" width="44" height="34" viewBox="0 0 44 34"><g fill="#b8cce4"><path d="M0 14 Q0 2 14 0 V7 Q7 8 7 14 H16 V34 H0Z"/><path d="M24 14 Q24 2 38 0 V7 Q31 8 31 14 H40 V34 H24Z"/></g></svg>
  <p class="abs quote-text italic">Temporibus autem quibusdam ets aut officiis debitis sit rerum neces sitatibus saepe eveniet ut et voluptates repudiandae Temporibus autem quibusdam et aut officiis debitis aut rerum necessitatibus saep.</p>
  <div class="abs q-line"></div>
  <div class="abs client-avatar" role="img" aria-label="Client portrait photo"></div>
  <div class="abs client-name">Daniel Herrera</div>
  <div class="abs client-role italic">Businessman</div>
</div>

<!-- free consultation -->
<div class="abs consult" role="img" aria-label="Dark photo of an attorney signing documents at a desk"></div>
<div class="abs consult-shade"></div>
<h2 class="abs consult-title" style="font-weight:400">Free Consultation</h2>
<p class="abs consult-sub italic">Suspe ndisse cursus mal suada faci lisis. Lorem ipsum dolor sit ametion consectetur elit.<br>Vesti bulum nec odio ipsum voluptatem accusa nt ium doloremque</p>
<div class="abs field" style="left:75px">Your Name*</div>
<div class="abs field" style="left:344px">Your Email*</div>
<div class="abs field" style="left:613px">Phone Number*</div>
<div class="abs field" style="left:883px">Practice Area
  <svg style="position:absolute;right:6px;top:4px" width="12" height="8" viewBox="0 0 12 8"><path d="M1 1 L6 6 L11 1" fill="none" stroke="#eee" stroke-width="1.5"/></svg>
</div>
<div class="abs field desc">Case Description*</div>
<div class="abs btn send">SEND REQUEST</div>

<!-- footer -->
<footer class="abs footer"></footer>
<div class="abs f-head" style="left:75px">NAVBARS</div>
<ul class="abs f-list">
  <li>Home</li><li>About Us</li><li>Attorney</li><li>Practice Areas</li><li>Blog</li><li>Contact Us</li>
</ul>
<div class="abs f-head" style="left:267px">NEWSLETTER</div>
<p class="abs f-text" style="left:267px;top:2695px;width:220px">Neque porro quisquam est qui dolorem ipsum quia</p>
<div class="abs email-input">Enter Email</div>
<div class="abs btn subscribe">SUBMIT</div>
<div class="abs f-head" style="left:575px">CONTACT INFO</div>
<p class="abs f-text" style="left:575px;top:2695px;width:285px"><span style="color:var(--brand)">Loreta Benavides-Kurtz</span> sed ut perspiciatis unde omnis iste natus error sit volup.</p>
<div class="abs contact-row" style="top:2762px">
  <svg width="26" height="26" viewBox="0 0 26 26"><circle cx="13" cy="13" r="12" fill="none" stroke="#333" stroke-width="1.5"/><path d="M9 7l2 2.5-1 1.5c.7 1.6 2 2.9 3.6 3.6l1.5-1 2.5 2-1 2c-4.5-.3-8-3.8-8.3-8.3z" fill="#333"/></svg>
  <span>1800 555 0187</span>
</div>
<div class="abs contact-row" style="top:2797px">
  <svg width="26" height="26" viewBox="0 0 26 26"><circle cx="13" cy="13" r="12" fill="none" stroke="#333" stroke-width="1.5"/><rect x="7" y="9" width="12" height="8" fill="none" stroke="#333" stroke-width="1.4"/><path d="M7 9l6 5 6-5" fill="none" stroke="#333" stroke-width="1.4"/></svg>
  <span>info@examplelaw.com</span>
</div>
<div class="abs f-logo">Benavides Kurtz Law</div>
<div class="abs f-head" style="left:900px;top:2716px">FOLLOW US</div>
<div class="abs social"><span></span><span></span><span></span><span></span></div>
<div class="abs copy-bar">Copyright © 2016 Benavides-Kurtz Law. All Rights Reserved</div>

</body>
</html>
```